Brightwater Court Services needs a business card

I need a business card design for a new company
For the last 10 years I have ran a tennis management company called Silver Hollow Racquet (www.silverhollowracquet.com)
The new company - Brightwater Court Services (BCS) will replace SHRA starting this winter
The goal of BCS will be to expand our operations into new clubs as well and a revenue stream from existing clubs with courtlinkhub.net
We plan to go regional in 2014 and then look outward from there

Target Market(s)

small to medium sized tennis facilities both public and private
Our market are the clubs - not the players
This includes private clubs, municipalities, recreation assc, etc

Industry/Entity Type

Business

Requirements
Must have
• Dale Huxley
• President
• 555-284-1937 Office
• 555-419-5062 Cell
• dhuxley@brightwatercourtservices.com
• www.brightwatercourtservices.com
Nice to have
• One of the unique benefits to a company joining BCS will be integration into our web based club software service - Courtlinkhub.net
• We have developed this turnkey service for small to medium sized clubs and re the exclusive providers of it
Should not have
• address or state

```html
<!DOCTYPE html>
<html lang="en">
<head>
<meta charset="utf-8">
<title>Brightwater Court Services – Business Card Front</title>
<link rel="stylesheet" href="https://fonts.googleapis.com/css2?family=Varela+Round&display=swap">
<style>
  :root {
    --card-yellow: #fccb0b;
    --card-white: #ffffff;
    --brand-grey: #7c9194;
    --crop-mark: #c8102e;
  }
  html, body {
    margin: 0;
    padding: 0;
    width: 680px;
    height: 1200px;
    overflow: hidden;
    background: var(--card-white);
  }
  .card-canvas {
    position: relative;
    width: 680px;
    height: 1200px;
  }
  .card-art {
    position: absolute;
    inset: 0;
    display: block;
  }
  .card-art .bleed-fill { fill: var(--card-yellow); }
  .card-art .wave-white { fill: var(--card-white); }
  .card-art .crop-marks line {
    stroke: var(--crop-mark);
    stroke-width: 1.5;
  }
  .brand-lockup {
    position: absolute;
    left: 0;
    right: 0;
    top: 770px;
    display: flex;
    align-items: center;
    justify-content: center;
    gap: 14px;
  }
  .brand-mark {
    width: 30px;
    height: 30px;
    border-radius: 50%;
    background: var(--card-yellow);
    flex: none;
  }
  .brand-name {
    margin: 0;
    font-family: "Varela Round", sans-serif;
    font-weight: 400;
    font-size: 60px;
    letter-spacing: -0.5px;
    color: var(--brand-grey);
    line-height: 1;
  }
</style>
</head>
<body>
  <main class="card-canvas">
    <svg class="card-art" viewBox="0 0 680 1200" width="680" height="1200" aria-hidden="true">
      <rect class="bleed-fill" x="58" y="58" width="564" height="1085"/>
      <path class="wave-white"
            d="M58 651
               C 170 560, 330 380, 470 374
               C 545 371, 595 440, 622 520
               L 622 896
               C 560 876, 450 868, 340 892
               C 220 918, 120 985, 58 1085 Z"/>
      <g class="crop-marks">
        <line x1="58" y1="0" x2="58" y2="40"/>
        <line x1="622" y1="0" x2="622" y2="40"/>
        <line x1="0" y1="78" x2="32" y2="78"/>
        <line x1="648" y1="78" x2="680" y2="78"/>
        <line x1="58" y1="1164" x2="58" y2="1200"/>
        <line x1="622" y1="1164" x2="622" y2="1200"/>
        <line x1="0" y1="1121" x2="32" y2="1121"/>
        <line x1="648" y1="1121" x2="680" y2="1121"/>
      </g>
    </svg>
    <div class="brand-lockup">
      <span class="brand-mark" aria-hidden="true"></span>
      <p class="brand-name">courtlinkhub</p>
    </div>
  </main>
</body>
</html>
```